Needed! Great Book Cover for New Ghost Story

I need an enticing cover (both e-book and print formats) for a new mystery/thriller about ghosts. This is more of a paranormal or psychological thriller, not horror. The title should be easily visible in thumbnail view.

The story: a man is found dead in a gutted building* and a ghost is blamed. The ghost is a miner from the 1930s and is tall, thin, wears a long tail jacket and stovepipe hat (think Cornelius Bramwell). I have in mind a corpse outline near the steps with a ghostly shadow looming, but I am open to all interpretations and ideas.
Other elements in the story: female reporter, snakes, mountains, a haunted hotel called The Heron, copper and gold. The murder weapon was a knife.

Title and author:
Hollow Lanterns by Marla Quent

*The book is set in the mountain town of Jerome, Arizona. Please consider incorporating my own photographs in the design. See attached files.

Target Market(s)

Pelorix customers looking for new books; book store browsers

Font styles to use
Serif
Sans Serif

Requirements
Must have
• Prominent title and author name in easy-to-read font
Nice to have
• My photo as background; subtle element of the colors of copper and/or gold

```html
<!DOCTYPE html>
<html lang="en">
<head>
<meta charset="utf-8">
<title>Hollow Lanterns — Marla Quent</title>
<link rel="stylesheet" href="https://fonts.googleapis.com/css2?family=Roboto+Condensed:wght@300;700&display=swap">
<style>
  :root {
    --panel-dark: #2b1c16;
    --panel-deep: #1a110d;
    --panel-warm: #3d2a20;
    --plaster: #cdb89c;
    --plaster-dim: #a8927a;
    --brick: #8e5440;
    --brick-dark: #4a2a1f;
    --shadow: #160e0b;
    --cream: #f1dcc0;
    --brick-light: #c98a6c;
    --brick-mid: #a86a52;
    --slate: #8d9aa6;
  }
  html, body {
    margin: 0;
    padding: 0;
    overflow: hidden;
    background: var(--panel-deep);
  }
  .cover {
    position: relative;
    width: 777px;
    height: 1200px;
    overflow: hidden;
    font-family: "Roboto Condensed", "Arial Narrow", sans-serif;
    background:
      radial-gradient(ellipse 260px 200px at 560px 420px, rgba(120, 70, 50, 0.35), transparent 70%),
      radial-gradient(ellipse 220px 260px at 640px 760px, rgba(90, 60, 45, 0.35), transparent 70%),
      linear-gradient(180deg, var(--panel-dark) 0%, var(--panel-warm) 40%, #2e1f18 70%, var(--panel-deep) 100%);
  }
  .cover-photo {
    position: absolute;
    left: 0;
    top: 0;
    width: 286px;
    height: 1200px;
    background:
      radial-gradient(ellipse 90px 260px at 90px 800px, rgba(20, 12, 9, 0.85), transparent 75%),
      radial-gradient(ellipse 70px 200px at 230px 700px, rgba(15, 10, 8, 0.8), transparent 75%),
      radial-gradient(ellipse 160px 80px at 150px 930px, rgba(190, 160, 130, 0.35), transparent 75%),
      radial-gradient(ellipse 200px 120px at 190px 60px, rgba(110, 60, 40, 0.6), transparent 75%),
      linear-gradient(180deg,
        #6a3f2e 0%,
        var(--plaster-dim) 10%,
        var(--plaster) 22%,
        #bba286 36%,
        var(--brick) 42%,
        var(--brick-mid) 48%,
        var(--brick-dark) 56%,
        #3a2a22 66%,
        #5c4a3c 76%,
        #3b2c23 86%,
        var(--shadow) 100%);
  }
  .title-word,
  .author-line {
    position: absolute;
    margin: 0;
    text-transform: uppercase;
    color: transparent;
    -webkit-background-clip: text;
    background-clip: text;
  }
  .title-word {
    writing-mode: vertical-rl;
    line-height: 0.82;
    white-space: nowrap;
  }
  .title-main {
    left: 340px;
    top: 30px;
    font-size: 180px;
    font-weight: 700;
    letter-spacing: -2px;
    background-image:
      repeating-linear-gradient(100deg, rgba(255, 240, 220, 0.25) 0 6px, transparent 6px 22px, rgba(120, 60, 40, 0.3) 22px 27px, transparent 27px 44px),
      linear-gradient(180deg, var(--brick-light) 0%, var(--cream) 12%, var(--brick-mid) 24%, var(--cream) 38%, var(--brick-light) 52%, var(--cream) 64%, var(--brick-mid) 78%, var(--brick-light) 100%);
  }
  .title-lead {
    left: 548px;
    top: 44px;
    font-size: 220px;
    font-weight: 300;
    letter-spacing: 22px;
    background-image:
      repeating-linear-gradient(80deg, rgba(255, 240, 220, 0.2) 0 5px, transparent 5px 20px, rgba(110, 55, 38, 0.3) 20px 24px, transparent 24px 40px),
      linear-gradient(180deg, var(--cream) 0%, var(--brick-light) 18%, var(--cream) 34%, var(--brick-mid) 50%, var(--cream) 64%, var(--slate) 78%, var(--slate) 100%);
  }
  .author-line {
    left: 366px;
    line-height: 1;
    white-space: nowrap;
    font-size: 100px;
  }
  .author-first {
    top: 898px;
    font-weight: 300;
    letter-spacing: 1px;
    background-image: linear-gradient(90deg, var(--cream) 0%, var(--brick-light) 55%, var(--cream) 100%);
  }
  .author-last {
    top: 1002px;
    font-weight: 700;
    letter-spacing: 3px;
    background-image:
      repeating-linear-gradient(95deg, rgba(255, 240, 220, 0.2) 0 5px, transparent 5px 18px),
      linear-gradient(90deg, var(--brick-light) 0%, var(--cream) 40%, var(--slate) 100%);
  }
</style>
</head>
<body>
  <main class="cover">
    <div class="cover-photo" role="img" aria-label="Photograph of a gutted brick building with crumbling plaster, dark doorways and a faint ghostly figure in a stovepipe hat"></div>
    <h1 class="title">
      <span class="title-word title-lead">Hollow</span>
      <span class="title-word title-main">Lanterns</span>
    </h1>
    <p class="author-line author-first">Marla</p>
    <p class="author-line author-last">Quent</p>
  </main>
</body>
</html>
```